Brightwave Travel and Tours

Hotel Reservations
Airline Ticketing
Day Tour

My business is a Travel agency. My services are issuing domestic and international tickets. Book room/hotel reservations local/international.
My color preference is apple green/orange/red/blue.
Images of beaches, tickets,luggage.

Industry/Entity Type

Business

```html
<!DOCTYPE html>
<html lang="en">
<head>
<meta charset="utf-8">
<title>Brightwave Travel and Tours – Business Card</title>
<link rel="stylesheet" href="https://fonts.googleapis.com/css2?family=Montserrat:wght@400;600;700&family=Source+Sans+3:wght@400&display=swap">
<style>
  :root {
    --backdrop: #a9a6a7;
    --card: #fbfbfb;
    --teal: #1b7597;
    --sky: #1a92d6;
    --brand: #1f6f8f;
    --mark: #3aaee0;
    --ink: #2f3a44;
    --contact: #25527a;
    --divider: #e4e4e4;
  }
  * { margin: 0; padding: 0; box-sizing: border-box; }
  html, body { width: 1200px; height: 1200px; overflow: hidden; }
  body { background: var(--backdrop); position: relative; font-family: "Montserrat", sans-serif; }

  .card {
    position: absolute;
    width: 712px;
    height: 416px;
    background: var(--card);
    border-radius: 28px;
    overflow: hidden;
  }
  .card--front { left: 238px; top: 120px; }
  .card--back  { left: 230px; top: 645px; }

  .brand {
    position: absolute;
    display: flex;
    flex-direction: column;
    align-items: center;
    color: var(--brand);
    font-family: "Montserrat", sans-serif;
    font-weight: 700;
    text-align: center;
    line-height: 1;
  }
  .brand__dot { border-radius: 50%; background: var(--mark); margin-bottom: 22px; }
  .brand__name { text-transform: uppercase; letter-spacing: 1px; }
  .brand__sub { text-transform: uppercase; letter-spacing: 2px; margin-top: 6px; }

  .card--front .brand { left: 0; right: 0; top: 70px; }
  .card--front .brand__dot { width: 150px; height: 150px; }
  .card--front .brand__name { font-size: 46px; }
  .card--front .brand__sub { font-size: 24px; }

  .services {
    position: absolute;
    left: 0; right: 0; bottom: 0;
    height: 56px;
    background: var(--teal);
    display: flex;
    justify-content: center;
    align-items: center;
    gap: 14px;
    color: #fff;
    font-size: 19px;
    font-weight: 400;
    letter-spacing: 0.6px;
  }
  .services__sep { width: 1.5px; height: 24px; background: #fff; }

  .card--back .brand { left: 40px; width: 340px; top: 78px; }
  .card--back .brand__dot { width: 120px; height: 120px; margin-bottom: 20px; }
  .card--back .brand__name { font-size: 36px; }
  .card--back .brand__sub { font-size: 19px; }

  .card__divider {
    position: absolute;
    left: 357px; top: 45px;
    width: 1px; height: 270px;
    background: var(--divider);
  }

  .contact { position: absolute; left: 389px; top: 98px; }
  .contact__name { font-size: 28px; font-weight: 600; color: var(--sky); letter-spacing: 0.5px; }
  .contact__title { font-family: "Source Sans 3", sans-serif; font-size: 17px; color: var(--ink); margin-top: 6px; }
  .contact__list { list-style: none; margin-top: 24px; font-family: "Source Sans 3", sans-serif; font-size: 18px; color: var(--contact); }
  .contact__list li { display: flex; align-items: center; height: 25.5px; }
  .contact__icon { width: 16px; height: 16px; margin-right: 18px; fill: var(--sky); }
  .contact__note { font-family: "Source Sans 3", sans-serif; font-size: 18px; color: var(--contact); margin-top: 6px; }

  .footer-strip {
    position: absolute;
    left: 0; bottom: 0;
    width: 400px; height: 27px;
    background: var(--sky);
  }
  .footer-web {
    position: absolute;
    right: 0; bottom: 0;
    width: 372px; height: 54px;
    background: var(--teal);
    clip-path: polygon(38px 0, 100% 0, 100% 100%, 0 100%);
    color: #fff;
    font-family: "Source Sans 3", sans-serif;
    font-size: 18px;
    display: flex;
    align-items: center;
    padding-left: 50px;
  }
</style>
</head>
<body>

<section class="card card--front">
  <div class="brand">
    <span class="brand__dot"></span>
    <span class="brand__name">Brightwave</span>
    <span class="brand__sub">Travel and Tours</span>
  </div>
  <div class="services">
    <span>Hotel Reservations</span>
    <span class="services__sep"></span>
    <span>Airline Ticketing</span>
    <span class="services__sep"></span>
    <span>Day Tour</span>
  </div>
</section>

<section class="card card--back">
  <div class="brand">
    <span class="brand__dot"></span>
    <span class="brand__name">Brightwave</span>
    <span class="brand__sub">Travel and Tours</span>
  </div>

  <div class="card__divider"></div>

  <div class="contact">
    <h1 class="contact__name">Your name</h1>
    <p class="contact__title">Your Title</p>
    <ul class="contact__list">
      <li>
        <svg class="contact__icon" viewBox="0 0 16 16"><path d="M1 6c0-2 3-3.5 7-3.5S15 4 15 6v1.2h-3.2V5.5H4.2v1.7H1zM4 8h8l2 6H2z"/></svg>
        +00 111 222 3333
      </li>
      <li>
        <svg class="contact__icon" viewBox="0 0 16 16"><path d="M1 3h14v10H1z M2 4l6 5 6-5" fill="var(--sky)"/><path d="M2 4.2l6 5 6-5" stroke="#fff" stroke-width="1.3" fill="none"/></svg>
        yourname@yourwebsite.com
      </li>
      <li>
        <svg class="contact__icon" viewBox="0 0 16 16"><circle cx="8" cy="8" r="7"/><path d="M1 8h14M8 1v14M3 4h10M3 12h10" stroke="#fff" stroke-width="1" fill="none"/><ellipse cx="8" cy="8" rx="3" ry="7" stroke="#fff" stroke-width="1" fill="none"/></svg>
        www.yourwebsite.com
      </li>
    </ul>
    <p class="contact__note">Your Long Commercial or business</p>
  </div>

  <div class="footer-strip"></div>
  <div class="footer-web">www.yourwebsite.com</div>
</section>

</body>
</html>
```